Kestrel Ridge Plumbing Business card & letter head design

We need a new business card and letter head for our plumbing company called kestrel ridge plumbing. attached is the companys logo. We provide domestic and commercial plumbing services in regional western Australia. We are after Something simple yet nice to look at and something that fits within the trade industry.

Target Market(s)

trade/building industry

Contact Information for Business Card

Tarek Holm
Manager
0481 362 714
enquiries@krplumbing.example.au
ABN: 47 153 806 924
PCL: 5318

Domestic & Commercial Plumbing
Tip Truck & Excavator hire

Colors

Designer to choose colors to be used in the design.

```html
<!DOCTYPE html>
<html lang="en">
<head>
<meta charset="utf-8">
<title>Kestrel Ridge Plumbing – Letterhead</title>
<link href="https://fonts.googleapis.com/css2?family=Open+Sans:wght@400&family=Roboto:wght@400;700&display=swap" rel="stylesheet">
<style>
  :root {
    --brand-blue: #1654a8;
    --ink: #3a3a3a;
    --ink-soft: #4a4a4a;
    --rule-grey: #55575b;
    --paper: #ffffff;
    --backdrop: #e4e2dc;
    --sign-tone: #e6e6e6;
  }
  html, body {
    margin: 0;
    padding: 0;
    width: 1200px;
    height: 1200px;
    overflow: hidden;
    background: var(--backdrop);
  }
  .letterhead {
    position: absolute;
    left: 210px;
    top: 48px;
    width: 780px;
    height: 1103px;
    background: linear-gradient(180deg, var(--paper) 0%, #f7f7f7 100%);
    box-shadow: 0 6px 24px rgba(0,0,0,0.18);
    overflow: hidden;
    font-family: "Open Sans", sans-serif;
    color: var(--ink);
  }
  .brand-name {
    position: absolute;
    left: 64px;
    top: 92px;
    margin: 0;
    font-family: "Roboto", sans-serif;
    font-weight: 700;
    font-size: 26px;
    line-height: 1.15;
    color: var(--brand-blue);
    letter-spacing: 0.3px;
  }
  .contact {
    position: absolute;
    right: 64px;
    top: 58px;
    margin: 0;
    padding: 0;
    list-style: none;
    font-family: "Roboto", sans-serif;
    font-size: 15px;
    color: var(--ink);
  }
  .contact li {
    display: flex;
    align-items: center;
    gap: 8px;
    line-height: 22px;
  }
  .contact svg { width: 13px; height: 13px; flex: none; }
  .letter-body {
    position: absolute;
    left: 96px;
    top: 280px;
    width: 620px;
    font-size: 14.5px;
    line-height: 1.52;
    color: var(--ink-soft);
  }
  .letter-body p { margin: 0 0 18px; }
  .letter-body .salutation { margin-bottom: 14px; }
  .signature {
    width: 120px;
    height: 70px;
    margin-top: 12px;
    background: var(--sign-tone);
    border-radius: 4px;
  }
  .footer-band {
    position: absolute;
    left: 0;
    bottom: 0;
    width: 780px;
    height: 140px;
  }
  .footer-band text {
    font-family: "Roboto", sans-serif;
  }
</style>
</head>
<body>
  <main class="letterhead">
    <h1 class="brand-name">Kestrel Ridge<br>Plumbing</h1>

    <ul class="contact">
      <li>
        <svg viewBox="0 0 16 16" aria-hidden="true"><path fill="var(--brand-blue)" d="M3.6 1.5l2.3 2.4-1.2 1.9c.9 2 2.5 3.6 4.5 4.5l1.9-1.2 2.4 2.3-1.3 2.3C6.9 14.3 1.7 9.1 1.3 2.8z"/></svg>
        0481 362 714
      </li>
      <li>
        <svg viewBox="0 0 16 16" aria-hidden="true"><rect x="1" y="3" width="14" height="10" fill="var(--brand-blue)"/><path d="M1.5 3.5L8 9l6.5-5.5" fill="none" stroke="#fff" stroke-width="1.3"/></svg>
        enquiries@krplumbing.example.au
      </li>
    </ul>

    <section class="letter-body">
      <p class="salutation">Dear customer,</p>
      <p>Lorem ipsum dolor sit amet, consectetur adipisicing elit, sed do eiusmod tempor incididunt ut labore et dolore magna aliqua. Ut enim ad minim veniam, quis nostrud exercitation ullamco laboris nisi ut aliquip ex ea commodo consequat. Duis aute irure dolor in reprehenderit in voluptate velit esse cillum dolore eu fugiat nulla pariatur. Excepteur sint occaecat cupidatat non proident, sunt in culpa qui officia deserunt mollit anim id est laborum.</p>
      <p>Lorem ipsum dolor sit amet, consectetur adipisicing elit, sed do eiusmod tempor incididunt ut labore et dolore magna aliqua. Ut enim ad minim veniam, quis nostrud exercitation ullamco laboris nisi ut aliquip ex ea commodo consequat. Duis aute irure dolor in reprehenderit in voluptate velit esse cillum dolore eu fugiat nulla pariatur. Excepteur sint occaecat cupidatat non proident, sunt in culpa qui officia deserunt mollit anim id est laborum.</p>
      <p>Lorem ipsum dolor sit amet, consectetur adipisicing elit, sed do eiusmod tempor incididunt ut labore et dolore magna aliqua. Ut enim ad minim veniam, quis nostrud exercitation ullamco laboris nisi ut aliquip ex ea commodo consequat. Duis aute irure dolor in reprehenderit in voluptate velit esse cillum dolore eu fugiat nulla pariatur. Excepteur sint occaecat cupidatat non proident, sunt in culpa qui officia deserunt mollit anim id est laborum.</p>
      <p>Lorem ipsum dolor sit amet, consectetur adipisicing elit, sed do eiusmod tempor incididunt ut labore et dolore magna aliqua. Ut enim ad minim veniam, quis nostrud exercitation ullamco laboris nisi ut aliquip ex ea commodo consequat. Duis aute irure dolor in reprehenderit.</p>
      <p class="closing">Yours Sincerely,</p>
      <div class="signature" role="img" aria-label="Handwritten signature"></div>
    </section>

    <svg class="footer-band" viewBox="0 0 780 140" role="group" aria-label="Services and registration details">
      <path d="M0 132 L488 132 C510 132 515 84 540 84 L780 84 L780 140 L0 140 Z" fill="var(--brand-blue)"/>
      <path d="M0 125 L484 125 C506 125 511 77 536 77 L780 77" fill="none" stroke="var(--rule-grey)" stroke-width="4"/>
      <circle cx="64" cy="111" r="4" fill="var(--brand-blue)"/>
      <text x="73" y="116" font-size="14" fill="var(--ink)">Domestic &amp; Commercial Plumbing</text>
      <circle cx="296" cy="111" r="4" fill="var(--brand-blue)"/>
      <text x="305" y="116" font-size="14" fill="var(--ink)">Tip Truck &amp; Excavator hire</text>
      <text x="760" y="117" font-size="14" fill="#ffffff" text-anchor="end">ABN: 47 153 806 924  PCL: 5318</text>
    </svg>
  </main>
</body>
</html>
```